Brochure & Business card design

Looking for a new business card design i want it to be modern and sharp looking i usually order plastic business cards, and i would like to make the colors like the logo teal/charcoal i will like to have our services on icons with words.... our services are
ROOFING GUTTERS PAINTING PRESSURE WASHING EXTERIOR DESIGN & ATTIC VENTILATION. I also want to add my credentials

Target Market(s)

Oregon local market

Industry/Entity Type

Residential Construction

Contact Information for Business Card

Business info, services, number, website

Font styles to use
Serif
Sans Serif

Colors
33b8a4
5c5c5c
ffffff

Requirements
Must have
• Dale Finch
• Cell:
• Office:
• Email:
• Website:
• also i need our social media icons
• Services ROOFING GUTTERS PAINTING PRESSURE WASHING EXTERIOR DESIGN & ATTIC VENTILATION
• -icons for number, web, email, cell
• OR #584312
• Wa #KTRABLD461X7
Nice to have
• -Clean design Front & Back
• -Icons
• -shape House just like logo design
• -First Impression
Should not have
• Not Busy or lost of eye contact

```html
<!DOCTYPE html>
<html lang="en">
<head>
<meta charset="utf-8">
<title>Ridgeline Home Exteriors – Business Card</title>
<link rel="stylesheet" href="https://fonts.googleapis.com/css2?family=Montserrat:wght@400;500;600;700&display=swap">
<style>
  :root{
    --teal:#33b8a4;
    --charcoal:#5c5c5c;
    --white:#ffffff;
    --backdrop:#e9e9e9;
    --soft:#d7d7d7;
  }
  *{margin:0;padding:0;box-sizing:border-box}
  html,body{width:1200px;height:903px;overflow:hidden;background:var(--backdrop);font-family:"Montserrat",sans-serif}
  .stage{position:relative;width:1200px;height:903px}
  .card{position:absolute;top:297px;width:540px;height:309px;overflow:hidden;box-shadow:0 6px 18px rgba(0,0,0,.15)}
  .card--front{left:40px;background:var(--white)}
  .card--back{left:620px;background:var(--teal);display:flex;align-items:center;justify-content:center}
  .card-art{position:absolute;inset:0}

  .services{position:absolute;left:22px;top:14px;color:var(--white)}
  .services__title{color:var(--teal);font-weight:700;font-size:11px;letter-spacing:1px;margin:0 0 6px 150px}
  .services__cols{display:flex;gap:26px}
  .services__list{list-style:none;font-size:10.5px;font-weight:500}
  .services__list li{display:flex;align-items:center;gap:7px;height:16px}
  .services__list svg{width:11px;height:11px;stroke:var(--teal);fill:none;stroke-width:1.5}

  .contact{position:absolute;left:300px;top:98px;color:var(--white)}
  .contact__name{color:var(--teal);font-weight:700;font-size:21px;letter-spacing:1.5px;margin-bottom:10px}
  .contact__row{display:flex;align-items:flex-start;gap:9px;font-size:10.5px;font-weight:500;line-height:13px;margin-bottom:6px}
  .contact__icon{width:15px;height:15px;background:var(--teal);flex:none;display:flex;align-items:center;justify-content:center}
  .contact__icon svg{width:10px;height:10px;stroke:var(--white);fill:none;stroke-width:1.6}

  .brand{position:absolute;display:flex;align-items:center;gap:8px}
  .brand__mark{width:14px;height:14px;background:var(--teal);flex:none}
  .brand__name{color:var(--teal);font-weight:700;line-height:1.05;text-transform:uppercase}
  .card--front .brand{left:38px;top:150px}
  .card--front .brand__name{font-size:15px}
  .card--back .brand{position:static;gap:14px}
  .card--back .brand__mark{width:26px;height:26px;background:var(--charcoal)}
  .card--back .brand__name{color:var(--charcoal);font-size:28px}

  .footer{position:absolute;left:0;right:0;top:240px;padding:0 22px 0 222px;color:var(--charcoal)}
  .credentials{font-size:10px;font-weight:500;margin-bottom:8px}
  .footer__row{display:flex;align-items:center;gap:8px}
  .social{width:13px;height:13px;border-radius:50%;background:var(--charcoal)}
  .badge{margin-left:auto;width:52px;height:20px;background:#d23b32;border-radius:2px}
  .badge--dark{margin-left:6px;background:#1f1f1f}
</style>
</head>
<body>
<main class="stage">

  <section class="card card--front" aria-label="Business card front">
    <svg class="card-art" viewBox="0 0 540 309" aria-hidden="true">
      <path d="M0 0H540V228H252L208 136L108 80L14 128H0Z" fill="var(--charcoal)"/>
      <polyline points="0,134 14,134 108,87 203,140 246,234 540,234" fill="none" stroke="var(--teal)" stroke-width="3"/>
    </svg>

    <div class="services">
      <p class="services__title">SERVICES</p>
      <div class="services__cols">
        <ul class="services__list">
          <li><svg viewBox="0 0 12 12"><path d="M1 6L6 2L11 6M2.5 5V10H9.5V5"/></svg>Roofing</li>
          <li><svg viewBox="0 0 12 12"><path d="M1 3H11V5H1ZM9 5V11"/></svg>Gutters</li>
          <li><svg viewBox="0 0 12 12"><path d="M2 2H9V5H2ZM5.5 5V11"/></svg>Painting</li>
        </ul>
        <ul class="services__list">
          <li><svg viewBox="0 0 12 12"><path d="M1 4H6V7H1ZM6 5H9M9 3L11 1M9 5H11M9 7L11 9"/></svg>Pressure Washing</li>
          <li><svg viewBox="0 0 12 12"><path d="M1 1H11V11H1ZM1 6H11M6 1V11"/></svg>Exterior Design</li>
          <li><svg viewBox="0 0 12 12"><circle cx="6" cy="6" r="5"/><path d="M6 1V11M1 6H11"/></svg>Attic Ventilation</li>
        </ul>
      </div>
    </div>

    <div class="brand">
      <span class="brand__mark"></span>
      <span class="brand__name">Ridgeline<br>Home Exteriors</span>
    </div>

    <div class="contact">
      <h1 class="contact__name">DALE FINCH</h1>
      <p class="contact__row"><span class="contact__icon"><svg viewBox="0 0 10 10"><path d="M5 9.5C5 9.5 8.5 6 8.5 3.8A3.5 3.5 0 0 0 1.5 3.8C1.5 6 5 9.5 5 9.5Z"/><circle cx="5" cy="4" r="1.2"/></svg></span>Bend, OR 97701,<br>United States</p>
      <p class="contact__row"><span class="contact__icon"><svg viewBox="0 0 10 10"><path d="M2 1L4 3L3 4.5C3.8 6 4.5 6.7 5.5 7L7 6L9 8L7.5 9.5C4 9 1 6 .5 2.5Z"/></svg></span>(541) 555-0148</p>
      <p class="contact__row"><span class="contact__icon"><svg viewBox="0 0 10 10"><path d="M1 2H9V8H1ZM1 2L5 5.5L9 2"/></svg></span>hello@ridgelinehomes.com</p>
      <p class="contact__row"><span class="contact__icon"><svg viewBox="0 0 10 10"><circle cx="5" cy="5" r="4"/><path d="M1 5H9M5 1C3 3.5 3 6.5 5 9M5 1C7 3.5 7 6.5 5 9"/></svg></span>www.ridgelinehomes.com</p>
    </div>

    <div class="footer">
      <p class="credentials">OR #584312 | Wa #KTRABLD461X7</p>
      <div class="footer__row">
        <span class="social"></span><span class="social"></span><span class="social"></span>
        <span class="social"></span><span class="social"></span><span class="social"></span>
        <span class="social"></span><span class="social"></span>
        <span class="badge"></span><span class="badge badge--dark"></span>
      </div>
    </div>
  </section>

  <section class="card card--back" aria-label="Business card back">
    <div class="brand">
      <span class="brand__mark"></span>
      <span class="brand__name">Ridgeline<br>Home Exteriors</span>
    </div>
  </section>

</main>
</body>
</html>
```